Creative Real Estate Listing Mailer

I would like a creative double sided Real Estate listing flier/mailer to send out enticing people to list their house for sale with me. An example in my head, but feel free to be creative,.. would be one side with a Weiner dog with a sack of money on its back saying something like " its time to cash in" and the other side having some kind of southwest backdrop ( I live in Arizona) or luxury home, with my photo and my contact info saying something like list your house with me, or see what your home is worth etc.

Target Market(s)

People interested in selling their homes

Industry/Entity Type

Real Estate Agent

Contact Information for Business Card

Similar to the flyer, but simpler

Requirements
Must have
• My name: Milo Trask
My Email: milotrask@brevlo.com
My Phone# (480) 555 0147
Website www.Milotrask.com

```html
<!DOCTYPE html>
<html lang="en">
<head>
<meta charset="utf-8">
<title>Desert Crest Properties – Listing Mailer</title>
<link href="https://fonts.googleapis.com/css2?family=Anton&family=Montserrat:wght@300;500;700;800&display=swap" rel="stylesheet">
<style>
  :root{
    --maroon:#6b0d14;
    --blue:#2747a0;
    --orange:#e08a1e;
    --white:#ffffff;
    --ink:#1a1a1a;
    --rule:#999999;
    --bg:#e9e4dd;
  }
  *{box-sizing:border-box;margin:0;padding:0}
  html,body{width:1200px;height:1164px;overflow:hidden;background:var(--bg)}
  body{position:relative;font-family:'Montserrat',sans-serif;color:var(--ink)}
  .card{position:absolute;left:80px;width:1040px;height:530px;overflow:hidden;box-shadow:0 6px 18px rgba(0,0,0,.18)}
  .card--front{top:40px;background:linear-gradient(135deg,#fafafa,#e4e4e4)}
  .card--back{top:594px;background:var(--white)}
  .card svg.shapes{position:absolute;left:0;top:0}
  .abs{position:absolute}

  .brand{display:flex;align-items:center;gap:10px}
  .brand__mark{width:34px;height:34px;background:var(--maroon);flex:none}
  .brand__name{font-weight:800;font-size:18px;letter-spacing:1px;color:var(--ink);line-height:1.05;text-transform:uppercase;white-space:nowrap}

  /* front */
  .hero-art{left:520px;top:20px;width:300px;height:360px;border-radius:10px;
    background:radial-gradient(circle at 45% 55%,#3a2a20 0,#5a3e26 35%,#c9a476 70%,rgba(230,230,230,0) 100%)}
  .headline{left:70px;top:150px;font-family:'Anton',sans-serif;font-weight:400;color:var(--white);line-height:.95;text-transform:uppercase;text-shadow:0 3px 4px rgba(0,0,0,.35)}
  .headline__lead{font-size:62px;display:block}
  .headline__main{font-size:120px;display:block}
  .ribbon{left:78px;top:352px;background:var(--orange);color:var(--white);font-family:'Anton',sans-serif;font-size:32px;padding:4px 24px;border-radius:8px;letter-spacing:.5px}
  .call{left:70px;top:428px;color:var(--white)}
  .call__line{font-size:30px;font-weight:700;letter-spacing:1px;line-height:1.1}
  .call__line span{color:var(--orange);font-weight:300;margin-right:10px}
  .call__phone{display:flex;align-items:center;gap:12px;font-size:38px;font-weight:800;line-height:1.1;margin-top:4px}
  .icon-phone{width:40px;height:40px;flex:none}
  .social{left:880px;top:196px;width:110px;height:44px;border-radius:22px;background:var(--maroon);display:flex;align-items:center;gap:8px;padding-left:14px}
  .social__dot{width:26px;height:26px;border-radius:50%;background:var(--blue)}
  .badge-square{left:850px;top:292px;width:50px;height:50px;background:var(--ink)}
  .badge-frame{left:916px;top:282px;width:104px;height:60px;border:4px solid var(--blue);background:var(--white)}

  /* back */
  .photo-bg{left:0;top:0;width:700px;height:530px;
    background:linear-gradient(180deg,#e7c7d8 0%,#f4d9c2 35%,#b8a8a6 70%,#8d7f86 100%)}
  .agent-photo{left:300px;top:120px;width:300px;height:240px;border-radius:140px 140px 0 0;
    background:linear-gradient(180deg,#c79a80 0%,#1f2a4a 60%,#17203a 100%)}
  .pitch{left:40px;top:40px;font-weight:800;font-size:26px;line-height:1.25;color:var(--ink)}
  .pitch .hl-red{color:var(--maroon)}
  .pitch .hl-blue{color:var(--blue)}
  .name-tab{left:40px;top:360px;color:var(--white);font-weight:800;font-size:30px;line-height:40px;letter-spacing:1px}
  .contact{left:40px;top:420px;color:var(--white);list-style:none}
  .contact li{display:flex;align-items:center;gap:12px;font-size:17px;font-weight:500;line-height:1.3;margin-bottom:4px}
  .contact li.contact__phone{font-size:28px;font-weight:800}
  .contact svg{width:20px;height:20px;flex:none}
  .brand--back{left:740px;top:160px}
  .stamp{left:910px;top:30px;width:100px;height:110px;border:1.5px solid #777}
  .address-line{left:780px;width:230px;height:0;border-top:1.5px solid var(--rule)}
</style>
</head>
<body>

<!-- FRONT -->
<section class="card card--front" aria-label="Mailer front">
  <svg class="shapes" width="1040" height="530" viewBox="0 0 1040 530">
    <polygon points="600,180 1040,110 1040,170 600,250" fill="var(--maroon)"/>
    <polygon points="600,250 1040,170 1040,370 720,390 600,400" fill="var(--white)" opacity=".85"/>
    <polygon points="0,150 560,150 540,400 0,400" fill="var(--blue)"/>
    <path d="M0,400 L600,400 C660,400 680,372 740,372 L1040,350 L1040,362 L745,386 C690,386 670,416 610,416 L0,416 Z" fill="var(--blue)"/>
    <path d="M0,416 L610,416 C670,416 690,386 745,386 L1040,362 L1040,530 L0,530 Z" fill="var(--maroon)"/>
  </svg>

  <div class="abs brand" style="left:40px;top:34px">
    <div class="brand__mark"></div>
    <div class="brand__name">Desert Crest<br>Properties</div>
  </div>

  <div class="abs hero-art" role="img" aria-label="Photo of a dachshund beside a money sack with bundles of cash"></div>

  <h1 class="abs headline">
    <span class="headline__lead">Its Time To</span>
    <span class="headline__main">Cash In</span>
  </h1>
  <div class="abs ribbon">LIST YOUR HOUSE NOW</div>

  <div class="abs social" aria-label="Social links">
    <span class="social__dot"></span><span class="social__dot"></span>
  </div>

  <div class="abs badge-square"></div>
  <div class="abs badge-frame"></div>

  <div class="abs call">
    <div class="call__line"><span>CALL</span>MILO TRASK</div>
    <div class="call__phone">
      <svg class="icon-phone" viewBox="0 0 46 46"><circle cx="23" cy="23" r="21" fill="var(--blue)" stroke="var(--white)" stroke-width="3"/><path d="M17 13c1.5-1 3 2 4 4s-1 3-1 4 4 6 6 6 2-2 4-1 4 3 3 4-3 3-5 3c-6 0-15-9-15-15 0-2 2-4 4-5z" fill="var(--white)"/></svg>
      (480) 555 0147
    </div>
  </div>
</section>

<!-- BACK -->
<section class="card card--back" aria-label="Mailer back">
  <div class="abs photo-bg" role="img" aria-label="Southwest city skyline at sunset with mountains"></div>
  <div class="abs agent-photo" role="img" aria-label="Portrait of the agent in a navy suit"></div>
  <svg class="shapes" width="1040" height="530" viewBox="0 0 1040 530">
    <polygon points="0,410 330,410 350,345 640,345 625,530 0,530" fill="var(--maroon)"/>
    <polygon points="0,350 330,350 330,410 0,410" fill="var(--blue)"/>
    <polygon points="690,0 715,0 655,530 630,530" fill="var(--blue)"/>
    <polygon points="715,0 1040,0 1040,530 655,530" fill="var(--white)"/>
  </svg>

  <p class="abs pitch">List <span class="hl-red">Your House</span> with me,<br>or see what <span class="hl-blue">Your Home</span> is<br>worth.</p>

  <div class="abs name-tab">MILO TRASK</div>
  <ul class="abs contact">
    <li><svg viewBox="0 0 20 20"><rect x="2" y="4" width="16" height="12" fill="none" stroke="#fff" stroke-width="1.5"/><path d="M2 4l8 7 8-7" fill="none" stroke="#fff" stroke-width="1.5"/></svg>milotrask@brevlo.com</li>
    <li class="contact__phone"><svg viewBox="0 0 20 20"><circle cx="10" cy="10" r="8.5" fill="none" stroke="#fff" stroke-width="1.5"/><path d="M7 5.5c1-.5 2 1 2 2s-1 1 0 2.5 2 2 2.5 1.5 1.5 0 2.5.8-1 2.2-2 2.2c-3 0-6-3-6-6 0-1 .5-2 1-2.5z" fill="#fff"/></svg>(480) 555 0147</li>
    <li><svg viewBox="0 0 20 20"><circle cx="10" cy="10" r="8" fill="none" stroke="#fff" stroke-width="1.5"/><ellipse cx="10" cy="10" rx="3.5" ry="8" fill="none" stroke="#fff" stroke-width="1.2"/><path d="M2 10h16" stroke="#fff" stroke-width="1.2"/></svg>www.Milotrask.com</li>
  </ul>

  <div class="abs brand brand--back">
    <div class="brand__mark"></div>
    <div class="brand__name">Desert Crest<br>Properties</div>
  </div>
  <div class="abs stamp"></div>
  <div class="abs address-line" style="top:300px"></div>
  <div class="abs address-line" style="top:350px"></div>
  <div class="abs address-line" style="top:400px"></div>
</section>

</body>
</html>
```